Create Modern Clean Memorable Home Page

Please visit our current Homepage at www.brelvox.com. We want a fresh fun updated and memorable look. Feel free to use any of our photos if necessary. For more inspiration here are some other ice melt websites to browse:
http://www.quoralt.com/
http://www.pembrith.com/ice-melt/
http://www.globalvendrasalt.com/logistics.html
http://www.halvicsalt.com/
http://www.gubrine.com/
http://www.brinevaultco.com/gallery
http://www.thawfrost.com/products/calcium-chloride/
http://www.pelbranworks.com/dry-products
Updates
I have uploaded the logo
Just a note, we are not looking to simply display the product bags on the homepage. We want the first look at our page to pop and be memorable. We want color and possibly the use of photos with people and or animals and or landscapes to depict the use of the product. Most importantly it should be clean and not busy.
Industry/Entity Type
Logistics
Look and feel
Each slider illustrates characteristics of the customer's brand and the style your logo design should communicate.

```html
<!DOCTYPE html>
<html lang="en">
<head>
<meta charset="utf-8">
<title>Brelvox Seasonal Products</title>
<link href="https://fonts.googleapis.com/css2?family=Arimo:wght@400;700&family=Cabin:wght@400;500&display=swap" rel="stylesheet">
<style>
:root{
  --blue:#0a9bd3;
  --navy:#0b3572;
  --navy-dark:#062656;
  --text:#3a3a3a;
  --muted:#6a6a6a;
  --grey-btn:#4a4a4a;
  --footer:#141414;
  --line:#d9d9d9;
}
*{margin:0;padding:0;box-sizing:border-box}
html,body{width:1055px;height:1200px;overflow:hidden}
body{position:relative;background:#fff;font-family:"Arimo",Arial,sans-serif;color:var(--text)}
.abs{position:absolute}
.brand{display:flex;align-items:center;gap:8px;font-family:"Cabin",sans-serif;font-weight:400;color:var(--navy);white-space:nowrap}
.brand .mark{background:var(--blue);display:block;flex:none}
/* header */
.site-header{left:0;top:0;width:1055px;height:112px;background:linear-gradient(#fff,#eef1f4)}
.site-header .brand{left:90px;top:34px;font-size:30px}
.site-header .brand .mark{width:34px;height:34px}
.contact{right:102px;top:30px;text-align:right;font-family:"Cabin",sans-serif}
.contact .cta{color:var(--blue);font-size:15px}
.contact .phone-row{display:flex;align-items:center;gap:8px;justify-content:flex-end;margin-top:3px}
.contact .phone{font-family:"Arimo",sans-serif;font-size:29px;color:var(--navy);line-height:1}
.contact .mail{color:var(--blue);font-size:13px;margin-top:1px}
/* nav */
.main-nav{left:0;top:112px;width:1055px;height:46px;background:linear-gradient(var(--navy),var(--navy-dark));border-bottom:3px solid var(--blue);display:flex;padding-left:93px;font-family:"Cabin",sans-serif;font-size:14px}
.main-nav a{color:#fff;text-decoration:none;display:flex;align-items:center;padding:0 15px;height:40px;margin-top:6px;border-right:1px solid rgba(255,255,255,.12)}
.main-nav a:last-child{border-right:none}
.main-nav a.active{background:var(--blue);height:40px}
.main-nav a+a{margin-left:17px}
/* hero */
.hero{left:0;top:158px;width:1055px;height:382px;background:linear-gradient(90deg,#b9c4ce 0%,#dfe4ea 35%,#f1f3f6 65%,#fbfbfc 100%)}
.hero-panel{left:436px;top:61px;width:619px;height:180px;background:rgba(255,255,255,.8)}
.hero h1{left:453px;top:70px;font-size:46px;font-weight:700;color:var(--blue);letter-spacing:.5px;white-space:nowrap}
.hero p{left:457px;top:135px;width:500px;font-family:"Cabin",sans-serif;font-size:22px;line-height:30px;color:var(--navy-dark)}
.btn-more{left:457px;top:220px;width:202px;height:40px;background:linear-gradient(var(--navy),var(--navy-dark));border-radius:4px;color:#fff;font-family:"Cabin",sans-serif;font-size:17px;display:flex;align-items:center;justify-content:space-between;padding:0 10px 0 16px}
/* intro */
.intro{left:0;top:540px;width:1055px;height:200px;background:linear-gradient(#ececec,#fff 60%)}
.intro .brand{left:101px;top:40px;font-size:20px}
.intro .brand .mark{width:26px;height:26px}
.intro .divider{left:419px;top:30px;height:52px;border-left:1px dotted #999}
.signup-label{left:450px;top:43px;font-family:"Cabin",sans-serif;font-size:23px;color:var(--navy-dark)}
.signup-input{left:613px;top:41px;width:229px;height:30px;border:1px solid #ccc;background:#fff;font-size:12px;font-style:italic;color:#888;padding:8px}
.signup-btn{left:851px;top:41px;width:105px;height:30px;background:var(--blue);color:#fff;font-family:"Cabin",sans-serif;font-size:18px;display:flex;align-items:center;justify-content:center}
.intro-text{left:98px;top:97px;width:858px;font-size:11.4px;line-height:17.6px;text-align:justify}
.intro-text a{color:var(--blue);text-decoration:none}
/* cards */
.card{top:773px;width:283px;height:268px;border:1px solid #e2e2e2;background:linear-gradient(#fff 60%,#eeeeee)}
.card-head{height:59px;border-top:6px solid #0a86bd;background:var(--blue);color:#fff;font-family:"Cabin",sans-serif;font-size:24px;padding:15px 0 0 15px}
.card-head.navy{background:var(--navy);border-top-color:var(--navy-dark);padding-left:22px}
.card-body{padding:12px 14px;font-size:11.3px;line-height:17.6px;color:var(--muted);text-align:justify}
.photo{width:257px;height:86px;margin:0 -1px 10px;border:2px solid #cbd3db;background:linear-gradient(#5f8fc7,#3d6aa8 55%,#d8e1ea)}
.read-more{position:absolute;left:14px;bottom:11px;width:118px;height:32px;background:var(--grey-btn);color:#fff;font-family:"Cabin",sans-serif;font-size:18px;display:flex;align-items:center;justify-content:center}
.news{display:flex;align-items:center;height:52px;border-bottom:1px solid #fff;background:linear-gradient(#fafafa,#e9e9e9);padding-left:14px}
.news .day{font-family:"Cabin",sans-serif;font-size:31px;color:var(--blue);width:36px}
.news .mon{writing-mode:vertical-rl;transform:rotate(180deg);font-size:8px;color:#888;margin:0 6px 0 2px}
.news .sep{color:#bbb;font-size:22px;margin-right:10px}
.news .txt{font-family:"Cabin",sans-serif;font-size:13px;line-height:16px;color:#888}
/* footer */
.site-footer{left:0;top:1073px;width:1055px;height:127px;background:var(--footer);border-top:3px solid var(--blue);font-family:"Cabin",sans-serif;font-size:12.5px;color:#d8d8d8}
.foot-col{top:28px;line-height:21px}
.foot-rule{top:28px;height:85px;border-left:1px dotted #555}
.site-footer .brand{left:735px;top:25px;color:#cfcfcf;font-size:26px}
.site-footer .brand .mark{width:26px;height:26px;background:#cfcfcf}
.copy{left:742px;top:70px;font-family:"Arimo",sans-serif;font-size:11px;line-height:18px;color:#bbb}
</style>
</head>
<body>
<header class="site-header abs">
  <div class="brand abs"><span class="mark"></span>Brelvox seasonal products, inc.</div>
  <div class="contact abs">
    <div class="cta">For Appointment Call Us Today</div>
    <div class="phone-row">
      <svg width="24" height="34" viewBox="0 0 24 34" aria-hidden="true"><rect x="2" y="6" width="20" height="27" rx="2" fill="#222"/><rect x="15" y="0" width="3" height="8" fill="#222"/><rect x="5" y="10" width="14" height="7" fill="#ddd"/><g fill="#ddd"><rect x="5" y="20" width="3" height="2"/><rect x="10.5" y="20" width="3" height="2"/><rect x="16" y="20" width="3" height="2"/><rect x="5" y="24" width="3" height="2"/><rect x="10.5" y="24" width="3" height="2"/><rect x="16" y="24" width="3" height="2"/><rect x="5" y="28" width="3" height="2"/><rect x="10.5" y="28" width="3" height="2"/><rect x="16" y="28" width="3" height="2"/></g></svg>
      <div><div class="phone">555 014 2287</div><div class="mail">info@brelvoxseasonal.com</div></div>
    </div>
  </div>
</header>

<nav class="main-nav abs">
  <a class="active">Home</a><a>About Us</a><a>ICE Melters</a><a>Shovels &amp; ICE Choppers</a><a>Salt Spreaders</a><a>Snow Tools</a><a>Contact Us</a>
</nav>

<section class="hero abs" role="img" aria-label="Photo of a person clearing deep snow with a snow blower among snowy trees">
  <div class="hero-panel abs"></div>
  <h1 class="abs">BRELVOX SEASONAL</h1>
  <p class="abs">Manufacturer &amp; Nationwide Distributor of Ice Melt &amp; Snow Removal Products</p>
  <div class="btn-more abs">More Information
    <svg width="20" height="20" viewBox="0 0 20 20" aria-hidden="true"><circle cx="10" cy="10" r="9" fill="#fff"/><path d="M8 6l5 4-5 4z" fill="#0b3572"/></svg>
  </div>
</section>

<section class="intro abs">
  <div class="brand abs"><span class="mark"></span>Brelvox seasonal products, inc.</div>
  <div class="divider abs"></div>
  <div class="signup-label abs">Sign up Email:</div>
  <div class="signup-input abs">Email Address</div>
  <div class="signup-btn abs">Sign Up</div>
  <p class="intro-text abs">Brelvox Seasonal Products is one of America's premium producers of snow and ice removal products. Founded in 1993, Brelvox began as a small redistribution operation focused purely on rock salt. As the of America's premium producers of snow and ice removal products. Founded in 1993, Brelvox began as a small redistribution operation focused purely on rock salt. As the years passed we expanded our product line and began to manufacture our own products. We now produce a full line of snow and ice melters as well as snow shovels and car brushes. snow shovels and car brushes.<a>[Read More]</a>.</p>
</section>

<article class="card abs" style="left:92px">
  <div class="card-head">OUR MISSION</div>
  <div class="card-body">
    <div class="photo" role="img" aria-label="Photo of a jet boat with passengers speeding across a lake"></div>
    Brelvox Seasonal Products is one of America's premium producers of snow and ice removal products. Focused purely on rock salt.
  </div>
  <div class="read-more">READ MORE</div>
</article>

<article class="card abs" style="left:385px">
  <div class="card-head navy">BRELVOX SEASONAL</div>
  <div class="card-body" style="padding:12px 14px 0 16px">Brelvox Seasonal Products is one of America's premium producers of snow and ice removal products. Founded in 1993, Brelvox began as a small redistribution operation focused purely on rock salt. As the of America's premium producers of snow and ice removal products. Founded in 1993, Brelvox began as a small redistribution operation focused purely on rock salt.</div>
  <div class="read-more">READ MORE</div>
</article>

<article class="card abs" style="left:678px">
  <div class="card-head">NEWS &amp; EVENT</div>
  <div class="news"><span class="day">15</span><span class="mon">MAY</span><span class="sep">›</span><span class="txt">Lorem ipsum dolor sit dolor sit<br>amet, consectetuer adipiscing elit,</span></div>
  <div class="news"><span class="day">20</span><span class="mon">APR</span><span class="sep">›</span><span class="txt">Lorem ipsum dolor sit dolor sit<br>amet, consectetuer adipiscing elit,</span></div>
  <div class="news"><span class="day">07</span><span class="mon">MAR</span><span class="sep">›</span><span class="txt">Lorem ipsum dolor sit dolor sit<br>amet, consectetuer adipiscing elit,</span></div>
  <div class="read-more">READ MORE</div>
</article>

<footer class="site-footer abs">
  <div class="foot-col abs" style="left:134px">Quick Start Guide<br>About Us<br>Contact Us<br>Terms And Conditions</div>
  <div class="foot-rule abs" style="left:331px"></div>
  <div class="foot-col abs" style="left:381px;top:35px">Investor Reporting Platform<br>Investor And Board Reporting Resources<br>Board Reporting Principles</div>
  <div class="foot-rule abs" style="left:695px"></div>
  <div class="brand abs"><span class="mark"></span>Brelvox</div>
  <div class="copy abs">2013 BRELVOX , All Rights Reserved<br>Privacy Policy - Terms of Conditions.</div>
</footer>
</body>
</html>
```